Hi,

I would like to have a invitation made for a party. exactly like the picture in the link below.

http://pinboardia.example/pin/529174603381046725/

However, Please change the colors into fun/ girly feeling. font can be different and size of the card should be the same

Name of the girl: RUBA
What: Bachelorette Party
Where:TIKO Boat
Dubai Coral Sails Club
When:7th of February 2013

No RSVP required. (so no need to put it)

```html
<!DOCTYPE html>
<html lang="en">
<head>
<meta charset="utf-8">
<title>Ruba's Bachelorette Party Invitation</title>
<link rel="stylesheet" href="https://fonts.googleapis.com/css2?family=Alfa+Slab+One&family=Jost:wght@500&family=Open+Sans:wght@400;600&family=Oswald:wght@500&family=Righteous&display=swap">
<style>
  :root {
    --page-bg: #ffffff;
    --card-bg: #231f20;
    --ink-white: #ffffff;
    --accent-purple: #a3349b;
    --accent-green: #a6ce39;
    --ornament-grey: #d9d9d9;
  }
  * { box-sizing: border-box; margin: 0; padding: 0; }
  html, body {
    width: 1200px;
    height: 1001px;
    overflow: hidden;
    background: var(--page-bg);
  }
  .invitation {
    position: absolute;
    left: 40px;
    top: 233px;
    width: 1120px;
    height: 534px;
    background: var(--card-bg);
    overflow: hidden;
  }
  .headline-name {
    position: absolute;
    left: 24px;
    top: 112px;
    font-family: "Alfa Slab One", serif;
    font-size: 70px;
    line-height: 1;
    color: var(--accent-green);
    letter-spacing: 0.5px;
  }
  .headline-line {
    position: absolute;
    top: 199px;
    font-family: "Oswald", sans-serif;
    font-weight: 500;
    font-size: 56px;
    line-height: 1;
    color: var(--ink-white);
    white-space: nowrap;
  }
  .headline-line--left { left: 26px; }
  .headline-line--right { left: 406px; }
  .headline-single {
    position: absolute;
    top: 240px;
    font-family: "Jost", sans-serif;
    font-weight: 500;
    font-size: 218px;
    line-height: 1;
    color: var(--accent-purple);
    white-space: nowrap;
  }
  .headline-single--left { left: 20px; }
  .headline-single--right { left: 396px; }
  .corner-rule {
    position: absolute;
  }
  .details-panel {
    position: absolute;
    left: 792px;
    top: 48px;
    width: 206px;
    height: 454px;
    border: 3px solid var(--ink-white);
    border-radius: 32px;
    outline: 1px dotted var(--ornament-grey);
    outline-offset: -8px;
    display: flex;
    flex-direction: column;
    align-items: center;
    text-align: center;
    padding-top: 16px;
  }
  .details-label {
    font-family: "Righteous", sans-serif;
    font-size: 30px;
    line-height: 1;
    color: var(--accent-purple);
    margin-top: 12px;
  }
  .details-label:first-child { margin-top: 0; }
  .details-value {
    font-family: "Open Sans", sans-serif;
    font-weight: 600;
    font-size: 19px;
    line-height: 1.35;
    color: var(--ink-white);
    margin-top: 2px;
  }
  .details-value--small { font-size: 18px; }
  .details-note {
    font-family: "Open Sans", sans-serif;
    font-size: 15px;
    line-height: 1.15;
    color: var(--accent-purple);
    margin-top: 20px;
  }
  .details-rule { margin-top: 16px; }
</style>
</head>
<body>
  <main class="invitation">
    <svg class="corner-rule" style="left:270px;top:14px" width="110" height="72" viewBox="0 0 110 72">
      <path d="M2 2 H104 V70" fill="none" stroke="var(--ink-white)" stroke-width="2"/>
      <rect x="82" y="4" width="20" height="20" fill="var(--ornament-grey)" role="img" aria-label="Small knot ornament"/>
    </svg>
    <svg class="corner-rule" style="left:14px;top:470px" width="110" height="60" viewBox="0 0 110 60">
      <path d="M4 2 V56 H106" fill="none" stroke="var(--ink-white)" stroke-width="2"/>
      <rect x="6" y="32" width="20" height="20" fill="var(--ornament-grey)" role="img" aria-label="Small knot ornament"/>
    </svg>
    <svg class="corner-rule" style="left:436px;top:168px" width="282" height="30" viewBox="0 0 282 30">
      <line x1="0" y1="24" x2="282" y2="24" stroke="var(--ink-white)" stroke-width="2"/>
      <rect x="129" y="8" width="24" height="16" fill="var(--ornament-grey)" role="img" aria-label="Small knot ornament"/>
    </svg>

    <h1 class="headline-name">Ruba's</h1>
    <p class="headline-line headline-line--left">LAST CHANCE TO</p>
    <p class="headline-line headline-line--right">CELEBRATE BEING</p>
    <p class="headline-single headline-single--left">SIN</p>
    <p class="headline-single headline-single--right">GLE</p>

    <section class="details-panel">
      <h2 class="details-label">WHO</h2>
      <p class="details-value">Ruba</p>
      <h2 class="details-label">WHAT</h2>
      <p class="details-value details-value--small">Bachelorette Party</p>
      <h2 class="details-label">WHEN</h2>
      <p class="details-value details-value--small">7th of February 2013</p>
      <h2 class="details-label">WHERE</h2>
      <p class="details-value details-value--small">TIKO Boat<br>Dubai Coral Sails Club</p>
      <p class="details-note">The boat sails from<br>6 PM-10 PM</p>
      <svg class="details-rule" width="136" height="6" viewBox="0 0 136 6">
        <path d="M0 3 L64 1.5 L68 0 L72 1.5 L136 3 L72 4.5 L68 6 L64 4.5 Z" fill="var(--accent-green)"/>
      </svg>
    </section>
  </main>
</body>
</html>
```